120ml Jar Label — Masculine Cosmetic Foot Balm for Cracked, Hardworking Heels

We need a print-ready wraparound label for a 120ml jar — a brown/amber glass jar with a black metal screw lid (file photo attached).

--DO NOT PUT A BARCODE ON THE LABEL PLEASE--
**PLEASE READ "PLAN HUDDLE PROJECT BRIEF FINAL.MD" IN ATTACHED FILES IF YOU ARE SUBMITTING A DESIGN.**

The label is 190mm wide × 40mm high.
We need files to be in an .ai format with a 2mm bleed at the end.
Social media handle: @bramblekeepnz (facebook, instagram and tiktok)

Bramble Keep is a New Zealand foot-care brand making practical, no-nonsense products for hardworking men whose jobs wreck their feet. Our flagship product, Ridge Mender Balm, helps fix thick, cracked, hardworking skin.

Brand color scheme and overview is all in the brief file. You may add some brand aligned colors outside of the specified hex codes as you see fit to make a great design. Feel free to remove the "Bramble Keep" text from the logo so Bramble Keep is not doubled up on the front of the label

The tone we want: direct, rugged, and credible — like a workwear brand, not a spa brand. Most cracked-heel products on the market lean soft and feminine; we want to stand apart by looking like a serious fix for a real problem, made in New Zealand.

Full legal requirements for New Zealand cosmetic labelling (ingredients, directions, net contents, origin, etc.) are listed in the attached brief document — these are non-negotiable and must stay legible.

Please see the label attached "Label spacing guide" for this project's rough spacing guide. This label is the same size and sits well on the jar. This label doesn't need to be spaced quite as much as the Verin Label

I want to run the design for a week - I feel 7 days is a good amount of time for designers to see the work, digest the brief and create something remarkable and memorable for Bramble Keep.

Target Market(s)

Working men in New Zealand whose jobs or lifestyle put heavy wear on their feet — tradies, farmers, hospital/shift workers, hunters, and outdoors people. Practical, value-driven buyers rather than luxury skincare shoppers.

Industry/Entity Type

Beauty / Health & Wellness / Cosmetics

Font styles to use
Sans Serif
Other font styles liked:
• Montserrat (bold, headings), Inter (regular, body)

Colors
00AB8E
00BBA5
67D7C9
C6EFE9
E9F9F6
FFC000
F8CF3A
FAE287
FDF2CF
FEFAEE

Requirements
Must have
• All NZ cosmetic labelling requirements from the attached brief (product name, tag line, net contents, ingredients, directions, storage, made in NZ) — legible and complete, not omitted for aesthetics Fits 190mm × 40mm wraparound format for a 120ml brown jar with black lid Uses our existing brand colors: Deep Olive #3C4A34, Bone White #F4EFE6, Terracotta Clay #C1683D, and Warm Grey #4A4540 (exact palette in attached brief) Uses Montserrat (headings) and Inter (body) or close equivalents Incorporates our existing shield-and-wing logo (attached) Brand name and product name clearly readable from a normal shelf/bathroom-cabinet distance
Nice to have
• A style that could extend into a hero/product photo later, similar to the NZ-hills-backdrop look on our website (screenshot attached) — not required for the label itself, just good to keep in mind Original icon work (e.g. a small soak/apply/sock icon set) if it fits the rugged brand feel A design that could work as a small back-label/wraparound split if the front can't fit everything at a readable size
Should not have
• No pastel colors, floral motifs, or delicate script fonts — this should never look like spa/luxury skincare. Don't introduce new brand colors outside the palette provided other than black.

```html
<!DOCTYPE html>
<html lang="en">
<head>
<meta charset="utf-8">
<title>Bramble Keep — Ridge Mender Balm Jar Label</title>
<link href="https://fonts.googleapis.com/css2?family=Montserrat:wght@400;500;600;700;800&display=swap" rel="stylesheet">
<style>
  :root {
    --backdrop: #e4e4e4;
    --forest: #1c3a2e;
    --clay: #8b5a2c;
    --bone: #f4e6c9;
    --bone-soft: #e9dcc3;
    --text-light: #eef0ea;
  }
  * { margin: 0; padding: 0; box-sizing: border-box; }
  html, body {
    width: 1200px; height: 1200px; overflow: hidden;
    background: var(--backdrop);
    font-family: "Montserrat", sans-serif;
  }
  .label {
    position: absolute;
    left: 78px; top: 490px;
    width: 1044px; height: 219px;
    background: var(--forest);
    color: var(--text-light);
  }
  .info-block {
    position: absolute;
    font-size: 8px;
    line-height: 1.3;
    font-weight: 400;
  }
  .info-block strong { font-weight: 700; }
  .ingredients { left: 32px; top: 34px; width: 206px; }
  .caution { left: 32px; top: 125px; width: 220px; }
  .caution ul, .directions ol { list-style: none; }
  .caution li::before { content: "•"; margin-right: 4px; }
  .directions { left: 734px; top: 34px; width: 270px; }
  .directions li { padding-left: 10px; text-indent: -10px; }
  .net-qty { left: 734px; top: 139px; font-size: 9.5px; }
  .origin { left: 734px; top: 176px; font-size: 9.5px; }

  .brand-name {
    position: absolute;
    left: 352px; top: 146px; width: 136px;
    text-align: center;
    color: var(--bone);
    font-weight: 800;
    font-size: 17px;
    line-height: 1;
    letter-spacing: 0.2px;
  }
  .brand-name small { display: block; font-size: 8px; margin-top: 3px; }
  .brand-mark-area {
    position: absolute;
    left: 372px; top: 40px; width: 100px; height: 96px;
    background: linear-gradient(160deg, #5a3d25, #1c3a2e);
    border-radius: 8px;
    opacity: 0.55;
  }
  .accent-bar {
    position: absolute;
    left: 307px; top: 198px; width: 210px; height: 9px;
    background: var(--bone);
  }

  .product-panel { position: absolute; left: 497px; top: 0; width: 226px; height: 219px; }
  .product-panel svg { position: absolute; inset: 0; }
  .product-title {
    position: absolute; right: 13px; top: 25px;
    text-align: right;
    color: var(--bone);
    font-weight: 700;
    font-size: 25px;
    line-height: 1.08;
  }
  .rule { position: absolute; right: 13px; width: 74px; height: 1.5px; background: var(--bone-soft); }
  .rule-top { top: 118px; }
  .rule-bottom { top: 166px; }
  .tagline {
    position: absolute; right: 13px; top: 134px;
    text-align: right; font-size: 8px; line-height: 1.3; color: var(--bone-soft);
  }
  .volume {
    position: absolute; right: 13px; top: 176px;
    font-size: 15px; color: var(--bone);
  }
</style>
</head>
<body>
  <div class="label">
    <p class="info-block ingredients"><strong>Ingradients:</strong> Shea Butter, Beef Tallow, Beeswax, Grape Seed Oil, Vegetable Glycerin, Lanolin, Panthenol, Gluconolactone, Sodium Benzoate, Allantoin, Manuka Honey, Vitamin E, Tea Tree Essential Oil, Lemon Myrtle Essential Oil, Rosemary Oleoresin Extract</p>

    <div class="info-block caution">
      <p><strong>Caution:</strong></p>
      <ul>
        <li>For external use only.</li>
        <li>Do not apply to open wounds or infected skin.</li>
        <li>Avoid contact with eyes.</li>
        <li>Discontinue use if irritation occurs.</li>
        <li>Keep out of reach of children.</li>
      </ul>
    </div>

    <div class="brand-mark-area" role="img" aria-label="Brand emblem area"></div>
    <p class="brand-name">BRAMBLE KEEP<small>NZ</small></p>
    <div class="accent-bar"></div>

    <div class="product-panel">
      <svg width="226" height="219" viewBox="0 0 226 219" aria-hidden="true">
        <polygon points="40,0 226,0 226,219 40,219 0,183 0,40" fill="var(--clay)"/>
      </svg>
      <h1 class="product-title">RIDGE<br>MENDER<br>BALM</h1>
      <div class="rule rule-top"></div>
      <p class="tagline">Rugged NZ Foot Balm<br>for Cracked, Hardworking Heels</p>
      <div class="rule rule-bottom"></div>
      <p class="volume">120ml</p>
    </div>

    <div class="info-block directions">
      <p><strong>Directions:</strong></p>
      <ol>
        <li>1. Wash and dry your feet thoroughly.</li>
        <li>2. Apply a small amount of Ridge Mender Balm to clean, dry heels, focusing on dry, rough, or cracked areas.</li>
        <li>3. Massage gently until fully absorbed.</li>
        <li>4. For best results, use twice daily—morning and before bedtime.</li>
        <li>5. For intensive overnight care, apply generously and wear clean cotton socks after application.</li>
      </ol>
    </div>
    <p class="info-block net-qty">Net Qt. <strong>120ml</strong></p>
    <p class="info-block origin">Made in New Zealand</p>
  </div>
</body>
</html>
```